VALMIK GROUP

This is a company that provides executive protection. Our motto is "New Era in Protection"... I don't want this to look like other security websites. I want it to be clean and sharp and represent a new era. We are based in the bay area so maybe a picture of San Francisco in the background?
I want it to be able to funnel down a couple different categories.
1. About Us
2. Services (Executive Protection, Covert Protection, Residential Protection & Intelligence)
3. Blue Pike (Training & Consulting)
4. Contact Us
I want it to be very clean and modern. I don't want there to be any pictures of bodyguards with ear pieces like every other website.
Target Market(s)
Ultra High Net Worth Individuals
Coding
Coded - Design and coding required
Number of Pages Required
1 page
Requirements
Must have
- Colors of my Symbol
Nice to have
- City in the background, San Francisco, New York or the Thornmeadow Club in Montana.
Should not have
- Should not look like an KVM website or have photos of bodyguards. I want this to be a clean and simple website with my logo

```html
<!DOCTYPE html>
<html lang="en">
<head>
<meta charset="utf-8">
<title>VALMIK GROUP — New Era in Protection</title>
<link href="https://fonts.googleapis.com/css2?family=Exo+2:wght@400;600;700&family=Lato:wght@400;700&display=swap" rel="stylesheet">
<style>
:root{
  --red:#7e111b;
  --red-dark:#6a0d16;
  --ink:#1f1f1f;
  --text:#3c3c3c;
  --muted:#555;
  --paper:#ffffff;
  --gray:#f3f3f3;
  --charcoal:#262626;
  --footer:#1d1d1d;
}
*{margin:0;padding:0;box-sizing:border-box}
html,body{width:1200px;height:4231px;overflow:hidden}
body{position:relative;background:var(--paper);font-family:'Lato',sans-serif;color:var(--text)}
.abs{position:absolute}
.heading{font-family:'Exo 2',sans-serif;font-weight:700;color:var(--ink)}
.btn{position:absolute;display:flex;align-items:center;justify-content:center;background:var(--red);color:#fff;font-family:'Lato',sans-serif;font-weight:700;font-size:14px;letter-spacing:.3px;border-radius:3px;text-transform:uppercase;box-shadow:0 2px 5px rgba(0,0,0,.2)}
.rule{position:absolute;height:3px;background:var(--red)}

/* header */
.brand{position:absolute;left:144px;top:18px;width:160px;text-align:center;font-family:'Exo 2',sans-serif;font-weight:700;color:var(--ink);line-height:1}
.brand .name{font-size:30px;letter-spacing:1px}
.brand .sub{font-size:14px;letter-spacing:9px;margin-top:4px}
.brand .mark{width:26px;height:26px;background:var(--red);margin:0 auto 8px}
.phone{position:absolute;left:632px;top:28px;display:flex;align-items:center;gap:10px}
.phone .dot{width:34px;height:34px;border-radius:50%;background:var(--red);display:flex;align-items:center;justify-content:center}
.phone small{display:block;font-size:12px;color:var(--text)}
.phone b{font-family:'Exo 2',sans-serif;font-size:20px;color:var(--ink)}
.social{position:absolute;display:flex;gap:7px}
.social span,.fsocial span{border-radius:50%;display:flex;align-items:center;justify-content:center}
.social span{width:34px;height:34px;border:1.5px solid var(--ink)}
.nav{position:absolute;left:345px;top:95px;width:855px;height:48px;background:var(--red);clip-path:polygon(40px 0,100% 0,100% 100%,0 100%)}
.nav ul{list-style:none;display:flex;position:absolute;left:67px;top:0;height:48px;align-items:center;gap:54px}
.nav li{color:#fff;font-family:'Exo 2',sans-serif;font-weight:600;font-size:15px;position:relative}
.nav li.active:after{content:"";position:absolute;left:0;right:0;bottom:-14px;height:3px;background:#fff}

/* hero */
.hero{position:absolute;left:0;top:143px;width:1200px;height:665px;clip-path:polygon(0 0,100% 0,100% 92%,0 100%);
 background:
  radial-gradient(ellipse 60% 22% at 22% 42%,rgba(255,196,110,.85),rgba(255,196,110,0) 70%),
  radial-gradient(ellipse 45% 30% at 78% 18%,rgba(190,110,120,.55),rgba(190,110,120,0) 70%),
  linear-gradient(180deg,rgba(0,0,0,0) 45%,rgba(20,22,30,.55) 60%,rgba(14,16,22,.9) 100%),
  linear-gradient(180deg,#a46e74 0%,#d98a66 18%,#f0a865 33%,#c78764 42%,#514a55 52%,#2a2b35 70%,#1a1d25 100%)}
.hero h1{position:absolute;left:0;width:1200px;top:110px;text-align:center;font-size:54px;color:#111}
.dots{position:absolute;top:564px;left:563px;display:flex;gap:6px}
.dots span{width:20px;height:20px;border-radius:50%;border:2px solid #fff}

/* welcome */
.welcome-kicker{left:144px;top:868px;font-family:'Exo 2',sans-serif;font-size:27px;color:var(--ink)}
.welcome-title{left:144px;top:905px;font-size:37px}
.welcome-text{left:144px;top:986px;width:450px;font-size:16.5px;line-height:24px;color:var(--text)}
.welcome-photo{left:660px;top:876px;width:396px;height:420px;
 background:
  radial-gradient(ellipse 40% 35% at 55% 30%,rgba(120,170,230,.55),rgba(120,170,230,0) 70%),
  radial-gradient(ellipse 50% 30% at 40% 85%,rgba(70,120,170,.45),rgba(70,120,170,0) 70%),
  linear-gradient(160deg,#2a66a8 0%,#1b3c66 45%,#0f1b2e 100%)}

/* services */
.services-bg{left:0;top:1340px;width:1200px;height:800px;background:var(--gray);clip-path:polygon(0 0,100% 30px,100% 100%,0 100%)}
.section-title{left:0;width:1200px;text-align:center;font-size:37px}
.card{position:absolute;width:281px;height:499px;background:#fff;box-shadow:0 2px 8px rgba(0,0,0,.08);text-align:center}
.card .photo{height:230px}
.card h3{font-family:'Exo 2',sans-serif;font-weight:700;font-size:18px;color:var(--ink);margin-top:33px}
.card p{font-size:15px;line-height:22.5px;color:var(--muted);padding:0 18px;margin-top:10px}
.card .btn{left:75px;width:132px;height:38px;top:426px}

/* blue pike */
.pike{left:0;top:2134px;width:1200px;height:519px;background:var(--charcoal)}
.pike-photo{left:0;top:2134px;width:632px;height:519px;
 background:
  radial-gradient(ellipse 30% 25% at 40% 55%,rgba(235,235,240,.6),rgba(235,235,240,0) 70%),
  radial-gradient(ellipse 40% 30% at 25% 30%,rgba(180,130,100,.45),rgba(180,130,100,0) 70%),
  radial-gradient(ellipse 35% 40% at 80% 35%,rgba(60,50,45,.7),rgba(60,50,45,0) 70%),
  linear-gradient(180deg,#6e6256 0%,#8c8070 45%,#c9c4bc 72%,#5e5a55 100%);
 clip-path:polygon(0 0,100% 0,93% 100%,0 100%)}
.pike h2{position:absolute;left:681px;top:56px;font-size:37px;color:#fff}
.pike h4{position:absolute;left:681px;top:108px;font-family:'Exo 2',sans-serif;font-weight:400;font-size:27px;color:#fff}
.pike p{position:absolute;left:681px;top:186px;width:410px;font-size:16px;line-height:24px;color:#ddd}

/* blogs */
.blog-main-photo{left:144px;top:2840px;width:426px;height:279px;
 background:
  radial-gradient(ellipse 30% 20% at 25% 15%,rgba(255,230,170,.55),rgba(255,230,170,0) 70%),
  radial-gradient(ellipse 30% 20% at 75% 15%,rgba(255,230,170,.45),rgba(255,230,170,0) 70%),
  radial-gradient(ellipse 45% 35% at 50% 70%,rgba(40,90,100,.7),rgba(40,90,100,0) 70%),
  linear-gradient(160deg,#3c4e58,#1f2d35 55%,#7a5c3e)}
.blog-main{left:153px;top:3066px;width:407px;height:230px;background:#fff;border:1px solid #e2e2e2;text-align:center}
.blog-main h3{font-family:'Exo 2',sans-serif;font-weight:700;font-size:18px;line-height:26px;color:var(--ink);margin-top:18px}
.meta{font-size:13px;color:var(--red);font-weight:700}
.meta i{font-style:normal;color:#bbb;margin:0 10px}
.blog-main .meta{margin-top:14px}
.blog-main p{font-size:14px;line-height:22px;color:var(--muted);margin-top:14px;padding:0 30px}
.blog-side{position:absolute;left:593px;width:463px;height:215px}
.blog-side .box{position:absolute;left:190px;top:11px;width:263px;height:192px;background:#fff;padding:20px 22px}
.blog-side h4{font-family:'Exo 2',sans-serif;font-weight:700;font-size:14.5px;line-height:23px;color:var(--ink)}
.blog-side .meta{margin-top:8px;font-size:13px}
.blog-side p{font-size:13px;line-height:21px;color:var(--muted);margin-top:8px}

/* testimonials */
.testi{left:0;top:3392px;width:1200px;height:573px;
 background:
  radial-gradient(ellipse 25% 35% at 78% 30%,rgba(190,80,80,.45),rgba(190,80,80,0) 70%),
  radial-gradient(ellipse 20% 30% at 20% 45%,rgba(160,60,60,.35),rgba(160,60,60,0) 70%),
  linear-gradient(180deg,#861820 0%,#7b141c 55%,#5c0f16 100%)}
.testi h2{position:absolute;left:0;width:1200px;text-align:center;top:80px;font-size:37px;color:#fff}
.testi .rule{background:#fff;left:566px;top:141px;width:68px}
.testi blockquote{position:absolute;left:262px;top:180px;width:676px;text-align:center;font-size:17.5px;line-height:25.5px;color:#fff}
.avatars{position:absolute;top:333px;left:0;width:1200px;height:80px;display:flex;justify-content:center;align-items:center;gap:8px}
.avatars span{width:56px;height:56px;border-radius:50%;background:radial-gradient(circle at 50% 40%,#e6d2c2,#a98e7c);border:2px solid #fff}
.avatars span.on{width:76px;height:76px;border:3px solid #fff;background:radial-gradient(circle at 50% 40%,#f0e0d2,#b79c88)}
.arrow{width:20px;height:20px;margin:0 24px}
.testi .who{position:absolute;top:424px;left:537px;width:60px;text-align:center;font-size:12px;color:#fff;font-weight:700}

/* footer */
.footer{left:0;top:3965px;width:1200px;height:266px;background:var(--footer);color:#fff}
.finfo{position:absolute;top:48px;display:flex;gap:14px;font-size:15.5px;line-height:21px;color:#fff}
.fdiv{position:absolute;top:47px;width:1px;height:38px;background:#777}
.fline{position:absolute;left:350px;top:122px;width:730px;height:1px;background:#444}
.flinks{position:absolute;left:350px;top:156px;font-size:15px;color:#fff}
.copy{position:absolute;left:350px;top:190px;font-size:15px;color:#fff}
.fsocial{position:absolute;left:893px;top:165px;display:flex;gap:14px}
.fsocial span{width:36px;height:36px;border:1.5px solid #fff}
</style>
</head>
<body>

<!-- header -->
<div class="brand">
  <div class="mark"></div>
  <div class="name">VALMIK</div>
  <div class="sub">GROUP</div>
</div>
<div class="phone">
  <div class="dot"><svg width="16" height="16" viewBox="0 0 24 24"><path fill="#fff" d="M6.6 10.8a15 15 0 0 0 6.6 6.6l2.2-2.2a1 1 0 0 1 1-.25 11.4 11.4 0 0 0 3.6.57 1 1 0 0 1 1 1V20a1 1 0 0 1-1 1A17 17 0 0 1 3 4a1 1 0 0 1 1-1h3.5a1 1 0 0 1 1 1c0 1.25.2 2.45.57 3.57a1 1 0 0 1-.25 1z"/></svg></div>
  <div><small>Toll free :</small><b>+808 555 0142</b></div>
</div>
<div class="social" style="left:855px;top:30px">
  <span><svg width="16" height="16" viewBox="0 0 24 24" fill="none" stroke="#1f1f1f" stroke-width="2"><circle cx="12" cy="12" r="9"/><path d="M3 12h18M12 3c3 3 3 15 0 18M12 3c-3 3-3 15 0 18"/></svg></span>
  <span><svg width="16" height="16" viewBox="0 0 24 24" fill="none" stroke="#1f1f1f" stroke-width="2"><path d="M4 5h16v11H9l-5 4z"/></svg></span>
  <span><svg width="16" height="16" viewBox="0 0 24 24" fill="none" stroke="#1f1f1f" stroke-width="2"><rect x="3" y="5" width="18" height="14"/><path d="M3 5l9 7 9-7"/></svg></span>
  <span><svg width="16" height="16" viewBox="0 0 24 24" fill="none" stroke="#1f1f1f" stroke-width="2"><circle cx="6" cy="12" r="2.5"/><circle cx="18" cy="6" r="2.5"/><circle cx="18" cy="18" r="2.5"/><path d="M8 11l8-4M8 13l8 4"/></svg></span>
  <span><svg width="16" height="16" viewBox="0 0 24 24" fill="none" stroke="#1f1f1f" stroke-width="2"><path d="M10 14a4 4 0 0 0 6 0l3-3a4 4 0 0 0-6-6l-1 1M14 10a4 4 0 0 0-6 0l-3 3a4 4 0 0 0 6 6l1-1"/></svg></span>
</div>
<nav class="nav"><ul>
  <li class="active">HOME</li><li>ABOUT US</li><li>OUR SERVICES</li><li>BLUE PIKE</li><li>CONTACT US</li>
</ul></nav>

<!-- hero -->
<svg class="abs" style="left:0;top:740px" width="1200" height="70"><polygon points="700,70 1200,30 1200,14" fill="var(--red)"/></svg>
<section class="hero" role="img" aria-label="San Francisco skyline at sunset">
  <h1 class="heading">New Era in Protection</h1>
  <div class="btn" style="left:515px;top:197px;width:170px;height:46px">Learn More</div>
  <div class="dots"><span></span><span></span><span></span></div>
</section>

<!-- welcome -->
<div class="abs welcome-kicker">WELCOME TO</div>
<h2 class="abs heading welcome-title">VALMIK GROUP</h2>
<div class="rule" style="left:144px;top:966px;width:104px"></div>
<p class="abs welcome-text">Sed ut perspiciatis unde omnis iste natus voluptatem accusantium doloremque laudantium, totam rem aperiam, eaque ipsa quae ab illo inventore veritatis et quasi arcitecto beatae vitae dicta sunt explicabo. Nemo enim ipsam voltem quia voluptas sit aspernatur aut odit aut fugit, sed quia couuntur magni dolores eos qui ratione voluptatem sequi nesciunt. Neque porro quisquam est, qui dolorem ipsum quia dolor sit amet, consectetur, adipisci velit, sed quia non numquam eius modi</p>
<div class="btn" style="left:144px;top:1225px;width:149px;height:44px">Read More</div>
<div class="abs welcome-photo" role="img" aria-label="Security specialist at a monitoring workstation"></div>

<!-- services -->
<div class="abs services-bg"></div>
<h2 class="abs heading section-title" style="top:1418px">OUR SERVICES</h2>
<div class="rule" style="left:570px;top:1477px;width:60px"></div>

<div class="card" style="left:144px;top:1546px">
  <div class="photo" role="img" aria-label="Laptop with digital security interface" style="background:radial-gradient(ellipse 35% 30% at 45% 45%,rgba(140,210,255,.75),rgba(140,210,255,0) 70%),linear-gradient(135deg,#12345a,#3d7fb5 50%,#0e1d33)"></div>
  <h3>EXECUTIVE PROTECTION</h3>
  <p>Sed ut perspiciatis unde omnis sit voluptatem accusantium doloremque laudantium, totam rem aperiam, eaque ipsa quae ab illo inventore veritatis</p>
  <div class="btn">Read More</div>
</div>
<div class="card" style="left:460px;top:1523px">
  <div class="photo" role="img" aria-label="Analyst working at multiple monitors" style="background:radial-gradient(ellipse 30% 25% at 30% 40%,rgba(110,160,200,.6),rgba(110,160,200,0) 70%),linear-gradient(135deg,#1c2a38,#3e5568 50%,#10161d)"></div>
  <h3>COVERT PROTECTION</h3>
  <p>Sed ut perspiciatis unde omnis sit voluptatem accusantium doloremque laudantium, totam rem aperiam, eaque ipsa quae ab illo inventore veritatis</p>
  <div class="btn">Read More</div>
</div>
<div class="card" style="left:774px;top:1546px">
  <div class="photo" role="img" aria-label="Person using a tablet at home" style="background:radial-gradient(ellipse 25% 30% at 35% 30%,rgba(170,220,230,.6),rgba(170,220,230,0) 70%),radial-gradient(ellipse 40% 35% at 75% 70%,rgba(120,60,40,.5),rgba(120,60,40,0) 70%),linear-gradient(135deg,#b58a6a,#e2c7a8 50%,#6c4a3a)"></div>
  <h3>RESIDENTIAL PROTECTION</h3>
  <p>Sed ut perspiciatis unde omnis sit voluptatem accusantium doloremque laudantium, totam rem aperiam, eaque ipsa quae ab illo inventore veritatis</p>
  <div class="btn">Read More</div>
</div>

<!-- blue pike -->
<section class="abs pike">
  <h2 class="heading" style="color:#fff">BLUE PIKE</h2>
  <h4>TRAINING &amp; CONSULTING</h4>
  <p>Sed ut perspiciatis unde omnis iste natus voluptatem accusantium doloremque laudantium, totam rem aperiam, eaque ipsa quae ab illo inventore veritatis et quasi arcitecto beatae vitae dicta sunt explicabo. Nemo enim ipsam voltem quia voluptas sit aspernatur aut odit aut fugit, sed quia couuntur magni dolores eos qui ratione voluptatem sequi nesciunt. Neque porro quisquam est, qui dolorem ipsum quia dolor sit</p>
  <div class="btn" style="left:681px;top:407px;width:148px;height:44px">Read More</div>
</section>
<div class="abs pike-photo" role="img" aria-label="Team meeting around a laptop"></div>

<!-- blogs -->
<h2 class="abs heading section-title" style="top:2720px">LATEST BLOGS</h2>
<div class="rule" style="left:567px;top:2785px;width:66px"></div>

<div class="abs blog-main-photo" role="img" aria-label="Colleagues collaborating in an office"></div>
<article class="abs blog-main">
  <h3>SED UT PERSPICIATIS UNDE OMNIS<br>SIT VOLUPTATEM ACCUSAN</h3>
  <div class="meta">Jan 25, 2021<i>|</i>2 Comments</div>
  <p>Sed ut perspiciatis unde omnis iste natus error sit voluptatem accusantium doloremque laudantium, totam rem aperiam, eaque ipsa quae</p>
</article>

<article class="blog-side" style="top:2840px">
  <div class="abs" role="img" aria-label="Digital security lock on a device screen" style="left:0;top:0;width:463px;height:215px;background:radial-gradient(ellipse 25% 35% at 28% 50%,rgba(120,190,240,.7),rgba(120,190,240,0) 70%),linear-gradient(135deg,#0d2438,#1c4a6a 50%,#0a1522)"></div>
  <div class="box">
    <h4>NEMO ENIM IPSAM VOLUP<br>QUIA VOLUPTAS</h4>
    <div class="meta">Jan 25, 2021 &nbsp;&nbsp; 2 comments</div>
    <p>Sed ut perspiciatis unde omnis iste natus error sit vuptatem accusantium doloremque</p>
  </div>
</article>
<article class="blog-side" style="top:3080px">
  <div class="abs" role="img" aria-label="Operators in a monitoring room" style="left:0;top:0;width:463px;height:215px;background:radial-gradient(ellipse 30% 30% at 20% 35%,rgba(90,150,210,.55),rgba(90,150,210,0) 70%),linear-gradient(135deg,#12273d,#27496a 50%,#0b1523)"></div>
  <div class="box">
    <h4>NEMO ENIM IPSAM VOLUP<br>QUIA VOLUPTAS</h4>
    <div class="meta">Jan 25, 2021 &nbsp;&nbsp; 2 comments</div>
    <p>Sed ut perspiciatis unde omnis iste natus error sit vuptatem accusantium doloremque</p>
  </div>
</article>

<!-- testimonials -->
<section class="abs testi" role="img" aria-label="Client portrait faded in red">
  <h2 class="heading">TESTIMONIALS</h2>
  <div class="rule"></div>
  <blockquote>&ldquo; Lorem ipsum dolor sit amet, consectetur adipiscing elit, sed do eiusmod tempor incididunt ut labore et dolore magna aliqua. Ut enim ad minim veniam, quis nostrud exercitation ullamco laboris nisi ut aliquip ex ea commodo consequat. Duis aute irure dolor in reprehenderit in voluptate velit esse cillum dolore eu fugiat nulla pariatur. Excepteur sint occaecat cupidatat non proident &rdquo;</blockquote>
  <div class="avatars">
    <svg class="arrow" viewBox="0 0 20 20"><path d="M13 3 6 10l7 7" stroke="#fff" stroke-width="2" fill="none"/></svg>
    <span></span><span class="on"></span><span></span><span></span>
    <svg class="arrow" viewBox="0 0 20 20"><path d="M7 3l7 7-7 7" stroke="#fff" stroke-width="2" fill="none"/></svg>
  </div>
  <div class="who">JOHN DOE</div>
</section>
<svg class="abs" style="left:0;top:3890px" width="1200" height="76">
  <polygon points="0,76 0,55 463,22 1200,70 1200,76" fill="var(--footer)"/>
  <polyline points="0,55 463,22 1200,70" fill="none" stroke="#fff" stroke-width="3"/>
</svg>

<!-- footer -->
<footer class="abs footer">
  <div class="brand" style="left:123px;top:40px">
    <div class="mark" style="background:#fff"></div>
    <div class="name" style="color:#fff;font-size:34px">VALMIK</div>
    <div class="sub" style="color:#fff;font-size:17px">GROUP</div>
  </div>
  <div class="finfo" style="left:350px">
    <svg width="18" height="22" viewBox="0 0 18 22"><path d="M9 1a7 7 0 0 1 7 7c0 5-7 13-7 13S2 13 2 8a7 7 0 0 1 7-7z" fill="none" stroke="#fff" stroke-width="1.5"/><circle cx="9" cy="8" r="2.5" fill="none" stroke="#fff" stroke-width="1.5"/></svg>
    <div>Valmik Group<br>120 Harbor View Lane</div>
  </div>
  <div class="fdiv" style="left:622px"></div>
  <div class="finfo" style="left:650px">
    <svg width="20" height="20" viewBox="0 0 24 24"><path fill="none" stroke="#fff" stroke-width="1.5" d="M6.6 10.8a15 15 0 0 0 6.6 6.6l2.2-2.2a1 1 0 0 1 1-.25 11.4 11.4 0 0 0 3.6.57 1 1 0 0 1 1 1V20a1 1 0 0 1-1 1A17 17 0 0 1 3 4a1 1 0 0 1 1-1h3.5a1 1 0 0 1 1 1c0 1.25.2 2.45.57 3.57a1 1 0 0 1-.25 1z"/></svg>
    <div>Phone:<br>(808) 555 0142</div>
  </div>
  <div class="fdiv" style="left:842px"></div>
  <div class="finfo" style="left:870px">
    <svg width="22" height="16" viewBox="0 0 22 16"><rect x="1" y="1" width="20" height="14" fill="none" stroke="#fff" stroke-width="1.5"/><path d="M1 1l10 8 10-8" fill="none" stroke="#fff" stroke-width="1.5"/></svg>
    <div>E-mail:<br>info@valmikgroup.com</div>
  </div>
  <div class="fline"></div>
  <div class="flinks">Home &nbsp;|&nbsp; Services &nbsp;|&nbsp; About Us &nbsp;|&nbsp; Blue Pike &nbsp;|&nbsp; Contact Us</div>
  <div class="copy">© 2021 Valmik Group. All Rights Reserved.</div>
  <div class="fsocial">
    <span><svg width="16" height="16" viewBox="0 0 24 24" fill="none" stroke="#fff" stroke-width="2"><circle cx="12" cy="12" r="9"/><path d="M3 12h18M12 3c3 3 3 15 0 18M12 3c-3 3-3 15 0 18"/></svg></span>
    <span><svg width="16" height="16" viewBox="0 0 24 24" fill="none" stroke="#fff" stroke-width="2"><path d="M4 5h16v11H9l-5 4z"/></svg></span>
    <span><svg width="16" height="16" viewBox="0 0 24 24" fill="none" stroke="#fff" stroke-width="2"><rect x="3" y="5" width="18" height="14"/><path d="M3 5l9 7 9-7"/></svg></span>
    <span><svg width="16" height="16" viewBox="0 0 24 24" fill="none" stroke="#fff" stroke-width="2"><circle cx="6" cy="12" r="2.5"/><circle cx="18" cy="6" r="2.5"/><circle cx="18" cy="18" r="2.5"/><path d="M8 11l8-4M8 13l8 4"/></svg></span>
  </div>
</footer>

</body>
</html>
```